Bright oak path business card

Bright oak path is a new online life insurance company providing instant quotes and policies to consumers.
Target Market(s)
Target market is both business to business as well as business to consumer
Can think out side of the box- We are an open minded bunch
Industry/Entity Type
Life Insurance
Requirements
Must have
- Our corporate Logo
Double sided
Website www.brightoakpath.com.au
Phone Number
Name & Position of each person etc.
Modern font

```html
<!DOCTYPE html>
<html lang="en">
<head>
<meta charset="utf-8">
<title>Bright oak path business card</title>
<link rel="stylesheet" href="https://fonts.googleapis.com/css2?family=Michroma&display=swap">
<style>
  :root {
    --canvas: #ffffff;
    --ink: #231f20;
    --ink-soft: #8c8c8c;
    --sun: #f7c21c;
    --sun-pale: #fbe9a6;
    --citrus: #f6891f;
    --peach: #f7b48a;
    --lime-pale: #eef4c2;
    --shadow: rgba(0, 0, 0, 0.35);
  }
  * { margin: 0; padding: 0; box-sizing: border-box; }
  html, body {
    width: 1200px; height: 1200px; overflow: hidden;
    background: var(--canvas);
  }
  body { position: relative; font-family: "Michroma", sans-serif; color: var(--ink); }

  .card { position: absolute; overflow: hidden; }

  /* Front side */
  .card-front {
    left: 0; top: 0; width: 673px; height: 1040px;
    background: linear-gradient(90deg, var(--sun) 0%, var(--sun-pale) 40%, #ffffff 64%, #ffffff 100%);
    box-shadow: 3px 3px 4px var(--shadow);
    z-index: 2;
  }
  .brand-name {
    position: absolute; left: 38px; top: 48px;
    font-size: 56px; line-height: 1.22; font-weight: 400;
    color: var(--ink); letter-spacing: -1px;
  }
  .contact-block {
    position: absolute; left: 0; width: 673px; text-align: center;
  }
  .person-name { top: 462px; font-size: 33px; }
  .person-title { top: 540px; font-size: 20px; }
  .person-email { top: 625px; font-size: 24px; }
  .person-phone { top: 686px; font-size: 27px; }

  .stripe {
    position: absolute; left: 0; width: 100%;
    background: linear-gradient(180deg, rgba(246,137,31,0) 0%, var(--citrus) 50%, rgba(246,137,31,0) 100%);
  }
  .card-front .stripe-1 { top: 816px; height: 32px; }
  .card-front .stripe-2 { top: 910px; height: 34px; }
  .card-front .stripe-3 {
    top: 985px; height: 55px;
    background: linear-gradient(180deg, rgba(246,137,31,0) 0%, var(--citrus) 70%, var(--citrus) 100%);
  }

  /* Back side */
  .card-back {
    left: 676px; top: 408px; width: 499px; height: 767px;
    background: linear-gradient(90deg, #ffffff 0%, #ffffff 35%, var(--lime-pale) 100%);
    box-shadow: 3px 3px 4px var(--shadow);
    z-index: 1;
  }
  .brand-name-back {
    position: absolute; left: 24px; top: 40px;
    font-size: 40px; line-height: 1.3; color: var(--ink-soft); letter-spacing: -1px;
  }
  .back-block {
    position: absolute; left: 0; width: 499px; text-align: center;
  }
  .web-address { top: 352px; font-size: 20px; letter-spacing: -0.5px; }
  .postal-address { top: 428px; font-size: 22px; line-height: 38px; }

  .card-back .stripe {
    background: linear-gradient(180deg, rgba(247,180,138,0) 0%, var(--peach) 50%, rgba(247,180,138,0) 100%);
  }
  .card-back .stripe-1 { top: 602px; height: 22px; }
  .card-back .stripe-2 { top: 672px; height: 24px; }
  .card-back .stripe-3 { top: 738px; height: 29px;
    background: linear-gradient(180deg, rgba(247,180,138,0) 0%, var(--peach) 100%); }
</style>
</head>
<body>
  <section class="card card-front" aria-label="Card front">
    <div class="brand-name">Bright oak<br>path</div>
    <p class="contact-block person-name">Full Name</p>
    <p class="contact-block person-title">Job Title</p>
    <p class="contact-block person-email">email: email:email:email</p>
    <p class="contact-block person-phone">phone: 1300 275 275</p>
    <div class="stripe stripe-1"></div>
    <div class="stripe stripe-2"></div>
    <div class="stripe stripe-3"></div>
  </section>

  <section class="card card-back" aria-label="Card back">
    <div class="brand-name-back">Bright oak<br>path</div>
    <p class="back-block web-address">www.brightoakpath.com.au</p>
    <p class="back-block postal-address">Address: Level 18,<br>42 Harbour Lane<br>Eastwood Park<br>NSW 2190</p>
    <div class="stripe stripe-1"></div>
    <div class="stripe stripe-2"></div>
    <div class="stripe stripe-3"></div>
  </section>
</body>
</html>
```